Mini Book (4.25 x 6) Cover Design for Christian authors

We need a book cover designed for a mini book (4.25 x 6). We will need a front, back and spine for the book.
The book is titled:
Tender Lantern
Subtitle:
Quiet Echoes Along Your Path
Authors:
Walter and Joanna Brightmoor
We are wanting the colors Dark Blue and Grey with more blue than grey.
We do not want any stock images or photos, only original work.
The cover should convey sincerity, intuition and truth with prestige.
We want the back cover text to be included (top) and the bios to be on the back as well (bottom). *Those documents are included in the files.
Since it is a mini book, it is important for the design to be simple and not cluttered, but powerful!
This is the first book in a twelve book series, so we would like the same "look" to carry through all twelve books, eventually.
On the back of the book, at the bottom (left), we want the following contact information:
Morning Harvest Method Logo (in files below)
willowgatehaven@mailbrook.net
555.318.2046
P.O.Box 871
Fernhollow, ND 80199

Please save room on the back (bottom-right) for the ISBN and price.
Updates

Thank you to the designers that have submitted feedback concerning our design brief. We have made some changes that will perhaps make it easier to submit a variety of designs.Thank you! Added Saturday, March 4, 2017

Target Market(s)

Christians - mainly women

Industry/Entity Type

Religious

Font styles to use
Serif
Sans Serif
Decorative
Script
Other font styles liked:
• Not any particular font, looking for one that goes well with the cover design.

Requirements
Must have
• Mini Book Size (4.25 x 6)-spine size 1/8" (0.125)
• Dark blue and grey colors
• Cover needs to be simple and not cluttered or busy.
• Intriguing
• A font that is attractive, but it is still easy to read.
• *File information below
Nice to have
• Designs that are different from the mainstream.
• Perhaps a design that would do something different with the title/font? Maybe a repeat of the words from smaller to larger? Not sure how it would look, but maybe?
Should not have
• Any other colors but dark blue and grey
• Cluttered Look

```html
<!DOCTYPE html>
<html lang="en">
<head>
<meta charset="utf-8">
<title>Tender Lantern — Cover</title>
<link rel="stylesheet" href="https://fonts.googleapis.com/css2?family=Black+Ops+One&family=Parisienne&family=PT+Serif:wght@700&family=EB+Garamond:wght@400;700&family=Crimson+Text:ital@1&display=swap">
<style>
  :root {
    --page: #ffffff;
    --cover-blue: #0b46ef;
    --grey: #a9aab0;
    --grey-light: #d9dce6;
    --text-light: #e4e7f0;
  }
  * { margin: 0; padding: 0; box-sizing: border-box; }
  html, body { width: 720px; height: 1200px; overflow: hidden; background: var(--page); }
  .canvas { position: relative; width: 720px; height: 1200px; }

  .cover { position: absolute; left: 46px; width: 628px; height: 446px; background: var(--cover-blue); }
  .front { top: 109px; }
  .back { top: 664px; color: var(--text-light); font-family: "EB Garamond", serif; }

  .title { position: absolute; left: 102px; top: 92px; width: 400px; height: 110px; }
  .title text { font-family: "Black Ops One", sans-serif; fill: var(--grey-light); }

  .subtitle {
    position: absolute; left: 102px; top: 218px;
    font-family: "Parisienne", cursive; font-size: 29px; color: var(--grey-light); white-space: nowrap;
  }
  .rule { position: absolute; left: 102px; top: 294px; width: 428px; height: 6px; }
  .authors {
    position: absolute; left: 102px; top: 326px;
    font-family: "PT Serif", serif; font-weight: 700; font-size: 15px; color: var(--grey-light);
  }

  .blurb { position: absolute; left: 0; width: 628px; text-align: center; font-size: 13.2px; line-height: 15.6px; }
  .intro { top: 37px; }
  .promises { top: 96px; }
  .promises ul { list-style: none; font-weight: 700; }
  .promises li { line-height: 18px; }
  .promises li svg { width: 11px; height: 11px; vertical-align: -1px; margin-right: 5px; }
  .bio { top: 189px; line-height: 16.2px; }

  .verse {
    position: absolute; left: 150px; top: 266px; width: 300px; text-align: center;
    font-family: "Crimson Text", serif; font-style: italic; font-size: 15px; line-height: 18.6px;
  }
  .verse cite { display: block; font-family: "EB Garamond", serif; font-style: normal; font-size: 14px; line-height: 16px; }
  .quote-mark { position: absolute; width: 34px; height: 24px; }
  .quote-open { left: 124px; top: 262px; }
  .quote-close { left: 426px; top: 322px; }

  .publisher { position: absolute; left: 36px; top: 318px; display: flex; align-items: center; gap: 5px; }
  .publisher-dot { width: 30px; height: 30px; border-radius: 50%; background: var(--grey); flex: none; }
  .publisher-name { font-size: 10px; font-weight: 700; color: var(--text-light); white-space: nowrap; }
  .contact { position: absolute; left: 31px; top: 364px; font-size: 11px; line-height: 14.5px; font-style: normal; }
</style>
</head>
<body>
<main class="canvas">
  <section class="cover front" aria-label="Front cover">
    <svg class="title" viewBox="0 0 400 110" aria-label="Tender Lantern">
      <text x="0" y="48" font-size="58" textLength="300" lengthAdjust="spacingAndGlyphs">TENDER</text>
      <text x="0" y="106" font-size="58" textLength="345" lengthAdjust="spacingAndGlyphs">LANTERN</text>
    </svg>
    <p class="subtitle">Quiet Echoes Along Your Path</p>
    <svg class="rule" viewBox="0 0 428 6" preserveAspectRatio="none" aria-hidden="true">
      <path d="M0 3 Q100 1 214 2.5 T428 3 L428 4 Q300 5.5 200 4.5 T0 5 Z" fill="var(--grey)"/>
    </svg>
    <p class="authors">Authors: Walter and Joanna Brightmoor</p>
  </section>

  <section class="cover back" aria-label="Back cover">
    <p class="blurb intro">Morning Harvest Method (MHM)* proceeds, prepares and propels us into our Divine Inheritance.<br>God always has our best interest at heart. By understanding His power, we are able to significantly<br>impact the lives of others, leaving our imprint upon their hearts.</p>
    <div class="blurb promises">
      <p>This book will:</p>
      <ul>
        <li><svg viewBox="0 0 10 10" aria-hidden="true"><path d="M5 0 L10 5 L5 10 L0 5 Z" fill="var(--grey)"/></svg>Uncover the secret that is God’s plan</li>
        <li><svg viewBox="0 0 10 10" aria-hidden="true"><path d="M5 0 L10 5 L5 10 L0 5 Z" fill="var(--grey)"/></svg>Unveil God’s Six Significant Shields</li>
        <li><svg viewBox="0 0 10 10" aria-hidden="true"><path d="M5 0 L10 5 L5 10 L0 5 Z" fill="var(--grey)"/></svg>Unmask God’s Positioning Strategy (GPS)</li>
      </ul>
    </div>
    <p class="blurb bio">Joanna and Walter Brightmoor are international award-winning authors who inspire couples<br>and individuals to connect to the heart of God through Morning Harvest Method*.<br>For over twenty years, they have conducted workshops and seminars throughout the country and<br>at their private retreat center located in the Fernhollow hills.</p>

    <svg class="quote-mark quote-open" viewBox="0 0 36 26" aria-hidden="true">
      <path d="M2 26 C0 14 5 4 14 0 L15 3 C9 6 8 11 10 14 C14 15 16 18 15 22 C13 26 6 27 2 26 Z M21 26 C19 14 24 4 33 0 L34 3 C28 6 27 11 29 14 C33 15 35 18 34 22 C32 26 25 27 21 26 Z" fill="var(--grey)"/>
    </svg>
    <blockquote class="verse">
      Come, let us go up to the mountain of the Lord,<br>
      To the house (temple) of the God of Jacob;<br>
      That He may teach us His ways<br>
      And that we may walk in His paths.
      <cite>~ Isaiah 2:3~</cite>
    </blockquote>
    <svg class="quote-mark quote-close" viewBox="0 0 36 26" aria-hidden="true">
      <path d="M34 0 C36 12 31 22 22 26 L21 23 C27 20 28 15 26 12 C22 11 20 8 21 4 C23 0 30 -1 34 0 Z M15 0 C17 12 12 22 3 26 L2 23 C8 20 9 15 7 12 C3 11 1 8 2 4 C4 0 11 -1 15 0 Z" fill="var(--grey)"/>
    </svg>

    <div class="publisher">
      <span class="publisher-dot"></span>
      <span class="publisher-name">Morning Harvest Method</span>
    </div>
    <address class="contact">
      willowgatehaven@mailbrook.net<br>
      555.318.2046<br>
      P.O.Box 871<br>
      Fernhollow, ND 80199
    </address>
  </section>
</main>
</body>
</html>
```